Letterhead for clinic notes, test reports, and business cards

I need business card and letterheads for a medical clinic with the following:
1- Business cards. The back should allow for space for date and time of next appointments (few lines would do)
2- Letterhead for clinic notes
3- Letterhead for test reports.

Feel free to use whats included for examples. I value creativity so be creative.

Target Market(s)

Patients, referring physicians.

Industry/Entity Type

Health Care

Requirements
Must have
• Must use current logo.
• Must look good on white background
• Letterhead and reports must look good faxed.
• Please use themes of the current logo. Another possible color to use is grey as well (www.brackenvale-cardio.org - use the font color in the text of that website)

```html
<!DOCTYPE html>
<html lang="en">
<head>
<meta charset="utf-8">
<title>Brackenvale Cardiac Institute – Business Cards</title>
<link href="https://fonts.googleapis.com/css2?family=Questrial&display=swap" rel="stylesheet">
<style>
  :root{
    --bg:#e6e8eb;
    --cream:#f3efe4;
    --navy:#1c2f86;
    --blue-deep:#1b2d8a;
    --blue-mid:#1258b3;
    --blue-light:#1a9bd6;
    --red:#d42a2a;
    --ink:#3a3a3a;
    --line:#9a9a9a;
    --rule:#cfc9b8;
    --white:#ffffff;
  }
  *{box-sizing:border-box;margin:0;padding:0}
  html,body{width:1200px;height:786px;overflow:hidden}
  body{background:var(--bg);font-family:"Questrial",sans-serif;position:relative}
  .card{position:absolute;width:460px;height:263px;border-radius:16px;overflow:hidden;box-shadow:0 6px 18px rgba(0,0,0,.18)}
  .card--front{left:80px;top:80px;background:var(--cream)}
  .card--back{left:660px;top:80px;background:linear-gradient(115deg,var(--blue-deep) 0%,var(--blue-mid) 50%,var(--blue-light) 100%)}
  .card--appointment{left:370px;top:443px;background:var(--cream)}

  /* front */
  .swoosh{position:absolute;left:0;top:0;width:460px;height:263px}
  .brand{position:absolute;left:22px;top:56px;width:196px;display:flex;align-items:center;gap:8px}
  .brand__dot{width:12px;height:12px;border-radius:50%;background:var(--red);flex:none}
  .brand__name{font-size:14px;letter-spacing:1px;line-height:1.3;color:var(--navy);text-transform:uppercase}
  .divider{position:absolute;left:228px;top:52px;width:1px;height:128px;background:var(--rule)}
  .contact{position:absolute;left:242px;top:48px;color:var(--ink);font-size:11.5px;line-height:1.65}
  .contact__name{font-size:15px;color:var(--navy);letter-spacing:1px;text-transform:uppercase}
  .contact__role{margin-bottom:6px}
  .contact__row{display:flex;align-items:center;gap:6px;white-space:nowrap}
  .contact__icon{width:12px;height:12px;border-radius:2px;background:var(--red);flex:none;display:flex;align-items:center;justify-content:center}
  .contact__address{margin-top:6px}

  /* back */
  .back__brand{position:absolute;left:0;right:0;top:80px;display:flex;justify-content:center;align-items:center;gap:12px}
  .back__name{font-size:22px;letter-spacing:2px;line-height:1.25;color:var(--white);text-transform:uppercase;text-align:center}
  .back__url{position:absolute;left:0;right:0;top:170px;text-align:center;color:var(--white);font-size:13px;letter-spacing:.5px}

  /* appointment */
  .appt__brand{position:absolute;left:24px;top:20px;font-size:14px;letter-spacing:1px;color:var(--navy);text-transform:uppercase}
  .appt__title{position:absolute;right:24px;top:94px;font-size:14px;color:var(--red);letter-spacing:1px;text-transform:uppercase}
  .field{position:absolute;display:flex;align-items:flex-end;gap:6px;font-size:11px;color:var(--ink);text-transform:uppercase}
  .field__line{flex:1;border-bottom:1px solid var(--line);height:14px}
  .field--name{left:24px;top:48px;width:260px}
  .field--date{left:24px;top:74px;width:260px}
  .field--time{left:260px;top:120px;width:176px}
  .ampm{position:absolute;right:24px;top:140px;font-size:11px;color:var(--ink)}
  .days{position:absolute;left:24px;top:160px;display:flex;gap:18px;font-size:11px;color:var(--ink);text-transform:uppercase}
  .day{display:flex;align-items:center;gap:5px}
  .day__box{width:11px;height:11px;border:1px solid var(--ink)}
  .appt__note{position:absolute;left:24px;right:24px;top:208px;font-size:11px;color:var(--ink)}
</style>
</head>
<body>

<section class="card card--front" aria-label="Business card front">
  <svg class="swoosh" viewBox="0 0 460 263" aria-hidden="true">
    <path d="M0 150 C80 200 190 210 270 263 L0 263 Z" fill="var(--blue-mid)"/>
    <path d="M0 150 C80 200 190 210 270 263" fill="none" stroke="var(--white)" stroke-width="6"/>
    <path d="M0 140 C90 190 200 200 285 263" fill="none" stroke="var(--red)" stroke-width="5"/>
  </svg>
  <div class="brand">
    <span class="brand__dot"></span>
    <span class="brand__name">Brackenvale<br>Cardiac Institute</span>
  </div>
  <div class="divider"></div>
  <div class="contact">
    <p class="contact__name">Morgan Ellery</p>
    <p class="contact__role">General Manager</p>
    <p class="contact__row"><span class="contact__icon"><svg width="8" height="8" viewBox="0 0 8 8"><path d="M1 1 L3 1 L3.5 2.5 L2.6 3.2 C3 4.2 3.8 5 4.8 5.4 L5.5 4.5 L7 5 L7 7 C3.5 7 1 4.5 1 1Z" fill="#fff"/></svg></span>555-014-2287</p>
    <p class="contact__row"><span class="contact__icon"><svg width="8" height="8" viewBox="0 0 8 8"><rect x="1" y="1.5" width="6" height="5" fill="none" stroke="#fff" stroke-width="1"/></svg></span>555-014-9031</p>
    <p class="contact__row"><span class="contact__icon"><svg width="8" height="8" viewBox="0 0 8 8"><path d="M1 2 H7 V6 H1 Z M1 2 L4 4.5 L7 2" fill="none" stroke="#fff" stroke-width="1"/></svg></span>contact@brackenvale-cardio.org</p>
    <p class="contact__row"><span class="contact__icon"><svg width="8" height="8" viewBox="0 0 8 8"><circle cx="4" cy="4" r="3" fill="none" stroke="#fff" stroke-width="1"/></svg></span>www.brackenvale-cardio.org</p>
    <p class="contact__address">1870 Larch Avenue, Suite 204<br>Brackenvale ON K0L2P5</p>
  </div>
</section>

<section class="card card--back" aria-label="Business card back">
  <div class="back__brand">
    <span class="brand__dot"></span>
    <span class="back__name">Brackenvale Cardiac<br>Institute</span>
  </div>
  <p class="back__url">www.brackenvale-cardio.org</p>
</section>

<section class="card card--appointment" aria-label="Appointment card">
  <p class="appt__brand">Brackenvale Cardiac Institute</p>
  <div class="field field--name">Name <span class="field__line"></span></div>
  <div class="field field--date">Date <span class="field__line"></span></div>
  <p class="appt__title">Appointment Card</p>
  <div class="field field--time">Time <span class="field__line"></span></div>
  <p class="ampm">AM &nbsp; PM</p>
  <div class="days">
    <span class="day"><span class="day__box"></span>Mon.</span>
    <span class="day"><span class="day__box"></span>Tues.</span>
    <span class="day"><span class="day__box"></span>Wed.</span>
    <span class="day"><span class="day__box"></span>Thur.</span>
    <span class="day"><span class="day__box"></span>Fri.</span>
    <span class="day"><span class="day__box"></span>Sat.</span>
  </div>
  <p class="appt__note">If you are unable to keep your appointment, please call us within 24 hours.</p>
</section>

</body>
</html>
```